International freight forwarder experienced in perishable handling needs a web design

We need a website designed that will allow us to capture more customers through the website. We would like a visually appealing design that is not so heavy on text. Our business covers the logistics and freight forwarding industries and we have offices in South America and the USA. Our main customers are importers USA, Europe, Asia and Russia and we currently work almost exclusively with perishable products such as fresh cut flowers, fresh exotics fruits, cacao, fresh fish etc. We would like to convey a fresh, modern approach to freight forwarding focusing on concepts such as - time sensitive, anytime-anywhere delivery, innovation, experience, reliability and confidence. Should include links with Chatterpost and Workvine. Our core solutions include: Core Services
*Air Freight
*Ocean Freight
*Warehousing & Distribution
Our industry solutions cover
*Flowers
*FMCG including, fruits, vegetables
*Live animals
*Automotive
*Consumer Goods
*Industrial
*Oil & Gas
*Pharma
* Event logistics
* Project logistics

Target Market(s)

Importers in Europe, USA, Asia, Middle East and Russia

Number of Pages Required

4 page

Font styles to use
Sans Serif

Colors
a1cd39
606060
000000

Requirements
Must have
• Photos of fresh cut flowers, FMCG such as cacao, fresh fish (packaged for shipping), fresh exotic fruits, pharma products (packaged for shipping), oil and gas etc. Internal customer login access
Nice to have
• Photos of cargo shipping carriers and cargo airline carriers. Features similar to those of following website http://www.vantoshipping.example/eng/main/index.jsp?FromURL=web
Should not have
• Too much text, needs to be visually pleasing

```html
<!DOCTYPE html>
<html lang="en">
<head>
<meta charset="utf-8">
<title>Verdant Freight Group</title>
<link rel="stylesheet" href="https://fonts.googleapis.com/css2?family=Lato:ital,wght@0,400;0,700;0,900;1,400&family=Oxygen:wght@400;700&display=swap">
<style>
:root{
  --green:#a1cd39;
  --grey:#606060;
  --black:#000;
  --ink:#222;
  --panel:#2c2c2c;
  --panel-line:#555;
  --page-dark:#232323;
  --field:#c9c9c9;
  --white:#fff;
  --muted:#d6d6d6;
}
*{margin:0;padding:0;box-sizing:border-box}
html,body{width:1069px;height:1200px;overflow:hidden}
body{position:relative;font-family:'Lato',Arial,sans-serif;background:var(--page-dark);color:var(--white)}
.abs{position:absolute}

/* header */
.site-header{left:0;top:0;width:1069px;height:125px;background:var(--white)}
.brand{left:117px;top:64px;display:flex;align-items:center;gap:9px}
.brand-mark{width:17px;height:17px;border-radius:50%;background:var(--green)}
.brand-name{font-size:21px;font-weight:700;color:var(--grey);letter-spacing:-.3px}
.contact-phone{right:117px;top:23px;display:flex;align-items:center;gap:9px;font-size:17px;font-weight:700;color:var(--ink)}
.contact-mail{right:116px;top:57px;display:flex;align-items:center;gap:8px;font-size:12px;font-weight:700;color:var(--ink)}
.main-nav{left:357px;top:90px;display:flex;font-size:14px;color:var(--grey)}
.main-nav a{color:var(--grey);text-decoration:none;height:28px;line-height:28px}
.main-nav .active{background:var(--green);color:var(--ink);font-weight:700;padding:0 15px;border-radius:3px}

/* hero */
.hero{left:0;top:125px;width:1069px;height:398px;
  background:linear-gradient(180deg,#b9c4cc 0%,#9a8f86 30%,#8c6c5a 55%,#9f9c98 75%,#e2e2e2 100%)}
.hero-title{left:0;top:439px;width:1069px;text-align:center;font-family:'Oxygen',Arial,sans-serif;font-size:26px;font-weight:400;color:#111}

/* service tabs */
.service-tabs{left:125px;top:504px;width:818px;height:99px;display:flex;border-radius:3px;overflow:hidden;background:var(--black)}
.service{flex:1;display:flex;flex-direction:column;align-items:center;justify-content:flex-end;padding-bottom:18px;gap:12px;font-size:17px;color:var(--white)}
.service.current{background:#5c5c5c;border-top:8px solid var(--green)}
.service b{font-weight:700}

/* info panels */
.panel{top:642px;width:272px;height:277px;background:var(--panel);border:1px solid var(--panel-line);border-radius:3px;overflow:hidden}
.panel-head{position:absolute;left:0;top:0;width:272px;height:62px}
.panel-head svg{position:absolute;left:0;top:0}
.panel-dot{position:absolute;left:17px;top:4px;width:40px;height:40px;border-radius:50%;background:var(--white);border:3px solid #e8e8e8}
.panel-title{position:absolute;left:68px;top:9px;font-size:17px;font-weight:400;color:var(--ink)}
.panel-title b{font-weight:900}
.about-text{position:absolute;left:12px;top:62px;width:250px;font-size:12px;line-height:16.4px;letter-spacing:.3px;white-space:nowrap;color:var(--white)}
.more{position:absolute;left:8px;bottom:14px;width:95px;height:21px;background:var(--black);clip-path:polygon(0 0,100% 0,84% 100%,0 100%);font-size:12px;font-weight:700;line-height:21px;padding-left:8px;color:var(--white)}
.news-item{position:absolute;left:16px;width:245px;display:flex;gap:16px}
.date{width:42px;flex:none;text-align:center}
.date .day{background:var(--black);font-size:18px;font-weight:700;height:26px;line-height:26px}
.date .mon{background:#5a5a5a;font-size:11px;height:17px;line-height:17px}
.news-item h3{font-size:13px;font-weight:700;margin-bottom:6px;margin-top:-3px}
.news-item p{font-size:11px;line-height:16px;color:var(--muted)}
.news-rule{position:absolute;left:6px;top:137px;width:258px;border-top:1px dashed #4a4a4a}
.field{position:absolute;left:16px;width:240px;height:28px;background:var(--field);border-radius:3px;font-size:11px;font-style:italic;color:#555;padding:7px 15px}
.field.message{height:52px}

/* industry band */
.industry{left:0;top:953px;width:1069px;height:67px;background:var(--black)}
.industry-title{left:118px;top:962px;font-size:16px;font-weight:700;line-height:22px;color:var(--green)}
.industry-arrow{left:250px;top:953px}
.industry-item{font-size:13px;color:var(--white)}
.industry-item::before{content:"";display:inline-block;width:5px;height:5px;border-radius:50%;background:var(--green);margin-right:4px;vertical-align:2px}

/* newsletter */
.newsletter{left:0;top:1048px;width:1069px;height:42px;background:linear-gradient(180deg,#555 0%,#333 100%);border-top:1px solid #6a6a6a}
.news-label{left:117px;top:1058px;font-size:17px;color:var(--white)}
.news-input{left:313px;top:1057px;width:185px;height:24px;background:var(--black);border:1px solid #444;font-size:11px;font-style:italic;padding:5px 7px}
.news-btn{left:506px;top:1057px;width:76px;height:24px;background:var(--green);color:var(--ink);font-size:12px;font-weight:700;text-align:center;line-height:24px;border-radius:2px}
.follow-row{right:117px;top:1056px;height:28px;display:flex;align-items:center;gap:4px}
.follow{font-size:17px;color:var(--white);margin-right:6px}
.social{height:24px;line-height:22px;font-size:9px;font-weight:700;color:var(--white);background:#3a3a3a;border:1px solid #5a5a5a;border-radius:3px;padding:0 4px}

/* footer */
.site-footer{left:0;top:1091px;width:1069px;height:109px;background:#1f1f1f}
.footer-links{left:0;top:1108px;width:1069px;text-align:center;font-size:11px;color:var(--white)}
.footer-links span{margin:0 7px;color:#aaa}
.footer-contact{top:1139px;display:flex;align-items:center;gap:8px;font-size:12px;color:var(--white)}
.copyright{left:0;top:1173px;width:1069px;text-align:center;font-size:11px;color:var(--white)}
</style>
</head>
<body>

<header class="abs site-header"></header>
<div class="abs brand"><span class="brand-mark"></span><span class="brand-name">Verdant Freight Group</span></div>
<div class="abs contact-phone">
  <svg width="24" height="24" viewBox="0 0 24 24"><circle cx="12" cy="12" r="10.5" fill="none" stroke="#a1cd39" stroke-width="2"/><path d="M8.5 7c1 0 2 2 1.8 2.8-.2.6-1 .9-.7 1.6.5 1.2 1.5 2.2 2.7 2.7.7.3 1-.5 1.6-.7.8-.2 2.8.8 2.8 1.8 0 1.4-1.5 2-2.5 1.8-3.5-.6-6.7-3.8-7.3-7.3C6.7 8.5 7.3 7 8.5 7z" fill="#a1cd39"/></svg>
  123 456 7890
</div>
<div class="abs contact-mail">
  <svg width="19" height="12" viewBox="0 0 19 12"><rect width="19" height="12" fill="#111"/><path d="M0 0l9.5 7L19 0M0 12l7-6M19 12l-7-6" stroke="#fff" stroke-width="1.2" fill="none"/></svg>
  info@verdantfreightgroup.example
</div>
<nav class="abs main-nav">
  <a class="active">Home</a>
  <a style="margin-left:35px">About Us</a>
  <a style="margin-left:49px">Services</a>
  <a style="margin-left:49px">Our Network</a>
  <a style="margin-left:49px">News</a>
  <a style="margin-left:49px">Contact Us</a>
</nav>

<div class="abs hero" role="img" aria-label="Photo of palletised perishable cargo stacked beside a cargo aircraft on an airport apron"></div>
<h1 class="abs hero-title">Most Extensive Hub Operations In The ASEAN Region</h1>

<div class="abs service-tabs">
  <div class="service">
    <svg width="52" height="20" viewBox="0 0 52 20"><path d="M2 14c10 0 28-1 44-6 4-1 5 1 2 3-8 4-30 6-46 5zM22 12l8-10h4l-4 9zM20 14l6 5h4l-3-6zM4 13l-3-7h3l5 6z" fill="#fff"/></svg>
    <span>Air Freight</span>
  </div>
  <div class="service current">
    <svg width="48" height="26" viewBox="0 0 48 26"><path d="M2 14h44l-6 10H8zM12 8h22v6H12zM16 3h10v5H16zM20 0h3v3h-3z" fill="#fff"/><path d="M15 11h2M20 11h2M25 11h2M30 11h2" stroke="#5c5c5c" stroke-width="1.5"/></svg>
    <span><b>Ocean</b> Freight</span>
  </div>
  <div class="service">
    <svg width="42" height="28" viewBox="0 0 42 28"><path d="M2 10L21 1l19 9v2H2zM5 13h32v15h-4V17H9v11H5z" fill="#fff"/><path d="M11 19h20M11 22h20M11 25h20" stroke="#fff" stroke-width="2"/></svg>
    <span><b>Warehousing</b> &amp; Distribution</span>
  </div>
</div>

<section class="abs panel" style="left:119px">
  <div class="panel-head">
    <svg width="272" height="62" viewBox="0 0 272 62"><path d="M0 0H272V58Q150 30 0 44Z" fill="#a1cd39"/></svg>
    <span class="panel-dot"></span>
    <h2 class="panel-title">About <b>Verdant</b> Freight</h2>
  </div>
  <p class="about-text">Lorem ipsum dolor sit amet, consectet<br>adipiscing elit. Praesent vestibulum molestie<br>lacus. Aenean nonummy hendrerit mauris.<br>Phasellus por. Lorem ipsum dolor sit amet,<br>consectetuer adipisci elit. Praesent vestibulum<br>molestie lacus. An nonummy hendrerit mauris.<br>Phasellus porta. Lorem ipsum dolor sit amet,<br>consectetuer adipiscing Praesent vestibulum<br>molestie lacus. Aenean non hendrerit mauris.<br>Phasellus porta.Lorem ipsum</p>
  <a class="more">Read more »</a>
</section>

<section class="abs panel" style="left:399px">
  <div class="panel-head">
    <svg width="272" height="62" viewBox="0 0 272 62"><path d="M0 0H272V58Q150 30 0 44Z" fill="#a1cd39"/></svg>
    <span class="panel-dot"></span>
    <h2 class="panel-title"><b>Our</b> News</h2>
  </div>
  <div class="news-item" style="top:67px">
    <div class="date"><div class="day">01</div><div class="mon">APR</div></div>
    <div><h3>Lorem Ipsum Dolor Sit Ametc</h3><p>Lorem ipsum dolor sit amet, consectet uer adimpisciged diamr nonummy</p></div>
  </div>
  <div class="news-rule"></div>
  <div class="news-item" style="top:155px">
    <div class="date"><div class="day">02</div><div class="mon">APR</div></div>
    <div><h3>Biam nonummy nibh euismod</h3><p>Lorem ipsum dolor sit amet, consectet adimpiscigsed diamr nonummy nibh euismod tincidunt ut</p></div>
  </div>
  <a class="more">Read more »</a>
</section>

<section class="abs panel" style="left:679px">
  <div class="panel-head">
    <svg width="272" height="62" viewBox="0 0 272 62"><path d="M0 0H272V58Q150 30 0 44Z" fill="#a1cd39"/></svg>
    <span class="panel-dot"></span>
    <h2 class="panel-title"><b>Quick</b> Inquiry</h2>
  </div>
  <div class="field" style="top:64px">Full Name</div>
  <div class="field" style="top:100px">Email Address</div>
  <div class="field" style="top:138px">Phone  Number</div>
  <div class="field message" style="top:176px">Message</div>
  <a class="more" style="bottom:16px">Submit »</a>
</section>

<div class="abs industry"></div>
<div class="abs industry-title">Our Industry<br>Solutions Cover</div>
<svg class="abs industry-arrow" width="28" height="67" viewBox="0 0 28 67"><path d="M0 0L28 33L0 67Z" fill="#2a2a2a"/></svg>
<span class="abs industry-item" style="left:313px;top:965px">Flowers</span>
<span class="abs industry-item" style="left:393px;top:965px">FMCG including, fruits, vegetables</span>
<span class="abs industry-item" style="left:629px;top:965px">Live animals</span>
<span class="abs industry-item" style="left:732px;top:965px">Automotive</span>
<span class="abs industry-item" style="left:835px;top:965px">Consumer Goods</span>
<span class="abs industry-item" style="left:313px;top:991px">Industrial</span>
<span class="abs industry-item" style="left:405px;top:991px">Oil &amp; Gas</span>
<span class="abs industry-item" style="left:496px;top:991px">Pharma</span>
<span class="abs industry-item" style="left:577px;top:991px">Event logistics</span>
<span class="abs industry-item" style="left:697px;top:991px">Project logistics</span>

<div class="abs newsletter"></div>
<div class="abs news-label">Subscribe to newsletter</div>
<div class="abs news-input">Enter Email Here</div>
<div class="abs news-btn">Subscribe</div>
<div class="abs follow-row">
  <span class="follow">Follow us</span>
  <span class="social">Chatterpost</span>
  <span class="social">Chirpline</span>
  <span class="social">Workvine</span>
  <span class="social">Circlespace</span>
</div>

<footer class="abs site-footer"></footer>
<div class="abs footer-links">Home<span>|</span>About Us<span>|</span>Services<span>|</span>Our Network<span>|</span>News<span>|</span>Contact Us</div>
<div class="abs footer-contact" style="left:177px">
  <svg width="11" height="16" viewBox="0 0 11 16"><path d="M5.5 0A5.5 5.5 0 0 0 0 5.5C0 9.5 5.5 16 5.5 16S11 9.5 11 5.5A5.5 5.5 0 0 0 5.5 0z" fill="#a1cd39"/><circle cx="5.5" cy="5.5" r="2" fill="#1f1f1f"/></svg>
  12/F Harbourline Cargo Centre, 40 Tide Road, Kwai Chung, Hong Kong
</div>
<div class="abs footer-contact" style="left:580px">
  <svg width="13" height="14" viewBox="0 0 13 14"><path d="M2.5 0c1.2 0 2.4 2.4 2.1 3.3-.2.7-1.2 1-.8 1.9.6 1.4 1.8 2.6 3.2 3.2.9.4 1.2-.6 1.9-.8.9-.3 3.3.9 3.3 2.1 0 1.6-1.8 2.4-3 2.1C5 11.2 1.3 7.5.6 3.4.3 2 1 0 2.5 0z" fill="#a1cd39"/></svg>
  &nbsp;123 456 7890
</div>
<div class="abs footer-contact" style="left:706px">
  <svg width="14" height="9" viewBox="0 0 14 9"><rect width="14" height="9" fill="#a1cd39"/><path d="M0 0l7 5 7-5" stroke="#1f1f1f" stroke-width="1" fill="none"/></svg>
  info@verdantfreightgroup.example
</div>
<div class="abs copyright">© 2015 VerdantFreightGroup, All Right Reserved</div>

</body>
</html>
```